fresh noodle packaging

we need to rebrand our existing brand which base for asia market in australia, we need a fresher look which market for more western style.

i attached our existing product, involved two logo, we want to make all design into one brand only, ( Bao Tin instead of noodle quillon)

requirement:
trendy
fresh
economical
" looks" enviromental friendly
cost effective

one design as a signature and represent the company, expect to fit all type of noodle except text and color
Updates

Need extra days to review

Target Market(s)

supermarket e.g vantrel

Requirements
Must have
• remain color from our old packaging

```html
<!DOCTYPE html>
<html lang="en">
<head>
<meta charset="utf-8">
<title>Bao Tin Fresh Egg Noodle – Pack Front</title>
<link rel="stylesheet" href="https://fonts.googleapis.com/css2?family=Titan+One&family=Poppins:wght@400;600;700&family=Archivo:wght@400;700;900&display=swap">
<style>
  :root {
    --pack-blue: #1f3f96;
    --pack-red: #ee1c25;
    --pack-white: #ffffff;
    --ink-black: #0b0b0b;
    --noodle-light: #f4e7bd;
    --noodle-mid: #e6cf8f;
    --noodle-deep: #d4b670;
    --halal-green: #0f6b3e;
  }
  * { box-sizing: border-box; margin: 0; padding: 0; }
  html, body {
    width: 1200px; height: 1200px; overflow: hidden;
    background: var(--pack-white);
  }
  .canvas { position: relative; width: 1200px; height: 1200px; }
  .pack {
    position: absolute; left: 244px; top: 150px;
    width: 719px; height: 906px;
    font-family: "Poppins", sans-serif; color: var(--pack-white);
  }
  .pack-art { position: absolute; inset: 0; width: 719px; height: 906px; display: block; }

  .brand-mark {
    position: absolute; left: 48px; top: 62px;
    display: flex; align-items: center; gap: 8px;
    font-weight: 700; font-size: 22px; letter-spacing: 0.5px;
  }
  .brand-dot { width: 22px; height: 22px; border-radius: 50%; background: var(--pack-red); }

  .product-title {
    position: absolute; left: 50px; top: 150px;
    font-family: "Titan One", sans-serif; font-size: 49px; line-height: 56px;
    color: var(--ink-black);
    -webkit-text-stroke: 7px var(--pack-white);
    paint-order: stroke fill;
  }
  .claim {
    position: absolute; left: 52px; top: 274px;
    font-weight: 700; font-size: 15px; letter-spacing: 0.3px;
  }
  .maker {
    position: absolute; left: 52px; top: 341px;
    font-weight: 600; font-size: 16.5px;
  }
  .pack-details {
    position: absolute; left: 52px; top: 372px;
    font-size: 12.5px; line-height: 17px; font-weight: 400;
  }

  .nutrition {
    position: absolute; left: 56px; top: 530px; width: 124px; height: 188px;
    background: var(--pack-white); color: var(--ink-black);
    padding: 5px 6px;
    font-family: "Archivo", sans-serif; font-size: 5.2px; line-height: 1.2;
  }
  .nutrition h3 {
    font-family: "Archivo", sans-serif; font-weight: 900; font-size: 15px; line-height: 1;
    letter-spacing: -0.3px; padding-bottom: 3px;
    border-bottom: 3.5px solid var(--ink-black);
  }
  .nutrition .row {
    display: flex; justify-content: space-between;
    border-bottom: 0.6px solid var(--ink-black); padding: 2.2px 0;
  }
  .nutrition .row.thick { border-bottom-width: 2px; }
  .nutrition .indent { padding-left: 8px; }
  .nutrition b { font-weight: 900; }
  .nutrition .note { font-size: 3.6px; padding-top: 3px; padding-bottom: 3px; border-bottom: 2.5px solid var(--ink-black); }

  .ingredients {
    position: absolute; left: 203px; top: 527px; width: 215px;
    font-size: 10.6px; line-height: 19px;
  }
  .how-to-cook {
    position: absolute; left: 56px; top: 741px; width: 225px;
    font-size: 10.6px; line-height: 19px;
  }
  .label-lead { font-weight: 700; }

  .cert-badge {
    position: absolute; left: 204px; top: 612px; width: 72px; height: 72px;
    border-radius: 50%; background: var(--pack-white);
    display: flex; align-items: center; justify-content: center;
  }
  .cert-badge-core { width: 44px; height: 44px; border-radius: 50%; background: var(--halal-green); }
</style>
</head>
<body>
<div class="canvas">
  <section class="pack">
    <svg class="pack-art" viewBox="390 240 1151 1450" preserveAspectRatio="none" xmlns="http://www.w3.org/2000/svg">
      <defs>
        <linearGradient id="noodleTone" x1="0" y1="0" x2="1" y2="1">
          <stop offset="0" stop-color="var(--noodle-light)"/>
          <stop offset="0.5" stop-color="var(--noodle-mid)"/>
          <stop offset="1" stop-color="var(--noodle-deep)"/>
        </linearGradient>
      </defs>
      <g role="img" aria-label="Photograph of a close-up of wavy fresh egg noodles">
        <rect x="1000" y="240" width="541" height="1450" fill="url(#noodleTone)"/>
      </g>
      <polygon class="band-white" fill="var(--pack-white)"
        points="390,240 1110,240 1275,605 1112,965 1275,1330 1110,1690 390,1690"/>
      <polygon class="band-red" fill="var(--pack-red)"
        points="390,240 1095,240 1260,605 1097,965 1260,1330 1095,1690 390,1690"/>
      <polygon class="panel-blue" fill="var(--pack-blue)"
        points="390,240 1028,240 1193,605 1028,965 1193,1330 1028,1690 390,1690"/>
    </svg>

    <div class="brand-mark"><span class="brand-dot"></span><span>Bao Tin</span></div>

    <h1 class="product-title">Fresh Egg<br>Noodle</h1>
    <p class="claim">NO PERSERVATIVES</p>

    <p class="maker">Bao Tin Foods MFR</p>
    <p class="pack-details">Keep refrigerated or below 4ºC<br>Product of Australia<br>NET WT. 420g</p>

    <div class="nutrition">
      <h3>Nutrition Facts</h3>
      <div class="row thick"><b>Amount Per Serving</b></div>
      <div class="row"><span><b>Calories</b> 123</span><span>Calories from Fat 123</span></div>
      <div class="row"><span></span><b>% Daily Value*</b></div>
      <div class="row"><span><b>Total Fat</b> 123g</span><b>123%</b></div>
      <div class="row indent"><span>Saturated Fat 123g</span><b>123%</b></div>
      <div class="row indent"><span>Trans Fat 123g</span><span></span></div>
      <div class="row"><span><b>Cholesterol</b> 123mg</span><b>123%</b></div>
      <div class="row"><span><b>Sodium</b> 123mg</span><b>123%</b></div>
      <div class="row"><span><b>Total Carbohydrate</b> 123g</span><b>123%</b></div>
      <div class="row indent"><span>Dietary Fiber 123g</span><span></span></div>
      <div class="row indent"><span>Sugars 123g</span><span></span></div>
      <div class="row thick"><span><b>Protein</b> 123g</span><span></span></div>
      <p class="note">*Percent Daily Values are based on a 2,000 calorie diet. Your daily value may be higher or lower depending on your calorie needs.</p>
    </div>

    <p class="ingredients"><span class="label-lead">Ingredients:</span> Lorem ipsum dolor sit amet, consectetuer adipiscing elit, sed diam nonummy nibh euismod</p>

    <div class="cert-badge" role="img" aria-label="Halal certification badge"><span class="cert-badge-core"></span></div>

    <p class="how-to-cook"><span class="label-lead">How to cook:</span> Lorem ipsum dolor sit amet, consectetuer adipiscing elit, sed diam nonummy nibh euismod tincidunt ut laoreet dolore magna aliquam erat vo-lutpat. Ut wisi enim ad minim</p>
  </section>
</div>
</body>
</html>
```